Pilates Studio webdesign - Homepage design

Need a web design for this new Pilates studio.

1) Need elegant design that has great use of stock photos. See attached plumeframe lightbox. Use these for your designs
http://www.frameplume.com/search/lightbox/58120947

Be creative in how you use images. Could be a collage, or single image if design is strong.

2) Also see attached site map (PDF)

3) Please refer to this website for the "rollover section" on homepage. https://www.bookingacademy-varn.com/
We want similar functionality for "I'm Here Because"

4) See attached logos ZIP file.

5) My client kind of likes this website too:
http://motionhallq.com

Target Market(s)

mostly women

Number of Pages Required

2 page

Font styles to use
Sans Serif

Requirements
Must have
• strong design
• good use of stock image(s)
• logo included
Nice to have
• elegant design
Should not have
• not planning to build a long scrolling page.

```html
<!DOCTYPE html>
<html lang="en">
<head>
<meta charset="utf-8">
<title>Motion Hall – Pilates Studio</title>
<link href="https://fonts.googleapis.com/css2?family=Montserrat:wght@300;400;500;600;700&display=swap" rel="stylesheet">
<style>
:root{
  --slate:#536d8c;
  --slate-dark:#4a6080;
  --orange:#f28c1e;
  --blue:#2f86d6;
  --white:#ffffff;
  --text:#8a8a8a;
  --muted-bg:#f6f6f6;
  --line:#e2e2e2;
  --ink:#4a4a4a;
}
*{margin:0;padding:0;box-sizing:border-box}
html,body{width:1200px;height:2299px;overflow:hidden;background:var(--white)}
body{font-family:"Montserrat",Arial,sans-serif;color:var(--text);position:relative}
.abs{position:absolute}

/* top navigation */
.topbar{left:0;top:0;width:1200px;height:54px;background:var(--slate)}
.nav-link{top:21px;font-size:10.5px;line-height:12px;color:var(--white);letter-spacing:.1px;white-space:nowrap}
.btn{display:flex;align-items:center;justify-content:center;color:var(--white);font-size:11px;letter-spacing:.3px;white-space:nowrap}
.btn-orange{background:var(--orange)}
.btn-blue{background:var(--blue)}

/* brand */
.brand{display:flex;align-items:center;gap:10px}
.brand-dot{width:26px;height:26px;border-radius:50%;background:var(--orange)}
.brand-name{font-weight:700;color:var(--slate);letter-spacing:.5px;white-space:nowrap}
.logo-band{left:0;top:54px;width:1200px;height:89px;background:var(--white)}

/* hero */
.hero{left:0;top:143px;width:1200px;height:523px;background:linear-gradient(180deg,#5d6f86 0%,#7b8ca2 45%,#56677e 100%)}
.hero-title{left:0;top:376px;width:1200px;text-align:center;color:var(--white);font-size:25px;font-weight:300;letter-spacing:1px}
.hero-sub{left:0;top:421px;width:1200px;text-align:center;color:var(--white);font-size:12px;font-weight:300}

/* reasons */
.section-title{left:0;width:1200px;text-align:center;font-weight:700;letter-spacing:.5px}
.reason{width:128px;height:128px;border-radius:50%;background:var(--slate);color:var(--white);display:flex;align-items:center;justify-content:center;text-align:center;font-size:12px;line-height:18px;font-weight:300;padding-top:32px}
.reason.is-active{background:var(--orange)}
.reason-pointer{left:287px;top:930px;width:0;height:0;border-left:9px solid transparent;border-right:9px solid transparent;border-top:10px solid var(--orange)}
.reason-panel{left:201px;top:979px;width:798px;height:184px;border:1px solid var(--line)}
.panel-title{left:0;top:36px;width:100%;text-align:center;color:var(--orange);font-size:17px;font-weight:400}
.panel-text{left:30px;top:74px;width:736px;text-align:center;font-size:11.5px;line-height:23px;font-weight:300}

/* about */
.about{left:0;top:1207px;width:1200px;height:287px;background:var(--muted-bg)}
.about-photo{left:191px;top:1226px;width:223px;height:268px;background:linear-gradient(180deg,#c9b8a8 0%,#a99ac4 60%,#9a8cc0 100%)}
.about-title{left:349px;top:1292px;color:var(--slate);font-size:21px;font-weight:700;line-height:23px}
.about-text{left:486px;top:1290px;width:500px;font-size:11.5px;line-height:23px;font-weight:300}
.about-text p+p{margin-top:23px}

/* story */
.story{left:0;top:1494px;width:1200px;height:518px;background:linear-gradient(180deg,#56698a 0%,#4b5f7f 100%)}
.avatar{left:539px;top:1687px;width:110px;height:110px;border-radius:50%;border:5px solid var(--orange);background:linear-gradient(180deg,#b89c86,#7f6a5c)}
.story-name{left:0;top:1814px;width:1200px;text-align:center;color:var(--white);font-size:12px;font-weight:600}
.story-text{left:220px;top:1850px;width:760px;text-align:center;color:var(--white);font-size:10.5px;line-height:21px;font-weight:300}
.dot{top:1964px;width:10px;height:10px;border-radius:50%;background:var(--white)}
.dot.is-active{background:var(--orange)}

/* footer */
.footer-link{font-size:10.5px;line-height:12px;color:#555;white-space:nowrap}
.footer-rule{left:0;top:2252px;width:1200px;height:1px;background:var(--line)}
.copyright{left:0;top:2270px;width:1200px;text-align:center;font-size:10px;color:#555}
</style>
</head>
<body>

<header>
  <div class="abs topbar"></div>
  <nav>
    <span class="abs nav-link" style="left:159px">I'M HERE BECAUSE</span>
    <span class="abs nav-link" style="left:273px">ABOUT &nbsp;BRENNAN</span>
    <span class="abs nav-link" style="left:386px">WHAT IS MOTION HALL</span>
    <span class="abs nav-link" style="left:548px">SCHEDULING SESSIONS</span>
    <span class="abs nav-link" style="left:680px">REFFERRALS</span>
    <span class="abs nav-link" style="left:755px">CONTACT US</span>
    <span class="abs btn btn-orange" style="left:841px;top:12px;width:167px;height:29px">MAKE AN APPOINTMENT</span>
  </nav>
  <div class="abs logo-band"></div>
  <div class="abs brand" style="left:470px;top:84px">
    <span class="brand-dot"></span>
    <span class="brand-name" style="font-size:21px">MOTION HALL</span>
  </div>
</header>

<section>
  <div class="abs hero" role="img" aria-label="Woman hanging upside down on a pilates trapeze table in a bright studio, blue-grey toned"></div>
  <h1 class="abs hero-title">MOTION HALL</h1>
  <p class="abs hero-sub">Neque porro quisquam est qui dolorem ipsum quia dolor sit amet, consectetur</p>
  <span class="abs btn btn-blue" style="left:499px;top:461px;width:201px;height:34px;font-size:12px">MAKE AN APPOINTMENT</span>
</section>

<section>
  <h2 class="abs section-title" style="top:737px;color:var(--slate);font-size:21px">I'M HERE BECAUSE</h2>
  <div class="abs reason is-active" style="left:232px;top:805px">PILATES</div>
  <div class="abs reason-pointer"></div>
  <div class="abs reason" style="left:383px;top:805px">BACK &amp;<br>JOINT PAIN</div>
  <div class="abs reason" style="left:535px;top:805px">STRETCHING</div>
  <div class="abs reason" style="left:687px;top:805px">MOBILITY &amp;<br>STABILITY</div>
  <div class="abs reason" style="left:838px;top:805px">STRENGTHEN<br>BODY</div>
  <div class="abs reason-panel">
    <h3 class="abs panel-title">PILATES</h3>
    <p class="abs panel-text">Lorem ipsum dolor sit amet, consectetur adipiscing elit, sed do eiusmod tempor incididunt ut labore et dolore magna aliqua. Ut enim ad minim veniam, quis nostrud exercitation ullamco laboris nisi ut aliquip ex ea commodo consequat. Duis aute irure dolor in reprehenderit in voluptate velit esse cillum dolore eu fugiat nulla pariatur.</p>
  </div>
</section>

<section>
  <div class="abs about"></div>
  <div class="abs about-photo" role="img" aria-label="Smiling instructor in a lilac shirt with arms crossed"></div>
  <h2 class="abs about-title">ABOUT<br>BRENNAN</h2>
  <div class="abs about-text">
    <p>Sed ut perspiciatis unde omnis iste natus error sit voluptatem accusantium doloremque laudantium, totam rem aperiam, eaque ipsa quae ab illo inventore veritatis et quasi architecto beatae vitae dicta sunt explicabo.</p>
    <p>Nemo enim ipsam voluptatem quia voluptas sit aspernatur aut odit aut fugit, sed quia consequuntur magni dolores eos qui ratione voluptatem sequi nesciunt. Neque porro quisquam est, qui dolorem ipsum quia dolor sit amet,t</p>
  </div>
</section>

<section>
  <div class="abs story" role="img" aria-label="Faded photo of a woman stretching on pilates equipment, deep blue overlay"></div>
  <h2 class="abs section-title" style="top:1588px;color:var(--orange);font-size:21px">CUSTOMER'S SUCCESS STORY</h2>
  <div class="abs avatar" role="img" aria-label="Portrait of the client"></div>
  <p class="abs story-name">LEON HARTLEY</p>
  <p class="abs story-text">Sed ut perspiciatis unde omnis iste natus error sit voluptatem accusantium doloremque laudantium, totam rem aperiam, eaque ipsa quae ab illo inventore veritatis et quasi architecto beatae vitae dicta sunt explicabo. Nemo enim ipsam voluptatem quia voluptas sit aspernatur aut odit aut fugit, sed quia consequuntur magni dolores eos qui ratione voluptatem</p>
  <span class="abs dot is-active" style="left:563px"></span>
  <span class="abs dot" style="left:584px"></span>
  <span class="abs dot" style="left:605px"></span>
  <span class="abs dot" style="left:626px"></span>
</section>

<footer>
  <div class="abs brand" style="left:201px;top:2086px;gap:8px">
    <span class="brand-dot" style="width:22px;height:22px"></span>
    <span class="brand-name" style="font-size:15px">MOTION HALL</span>
  </div>
  <span class="abs footer-link" style="left:463px;top:2077px">I'M HERE BECAUSE</span>
  <span class="abs footer-link" style="left:463px;top:2099px">ABOUT &nbsp;BRENNAN</span>
  <span class="abs footer-link" style="left:463px;top:2122px">WHAT IS MOTION HALL</span>
  <span class="abs footer-link" style="left:463px;top:2144px">SCHEDULING SESSIONS</span>
  <span class="abs footer-link" style="left:463px;top:2167px">REFFERRALS</span>
  <span class="abs footer-link" style="left:463px;top:2189px">CONTACT US</span>
  <span class="abs footer-link" style="left:670px;top:2077px">SITEMAP</span>
  <span class="abs footer-link" style="left:670px;top:2099px">PRIVACY &amp; LEGAL</span>
  <span class="abs btn btn-orange" style="left:830px;top:2080px;width:169px;height:28px;font-size:10px">MAKE AN APPOINTMENT</span>
  <div class="abs footer-rule"></div>
  <p class="abs copyright">© 2016 COMPANY NAME &nbsp;|&nbsp; ALL RIGHTS RESERVED</p>
</footer>

</body>
</html>
```